Bref créative
RON TALIVERO STATIONARY PACKAGE
Letterhead paper, Envelopes, Business Cards, Patient brochures, Flyer,Gift Certificate, T-Shirts
Professional
RON TALIVERO DDS
General & Cosmetic Dentistry
47-30 91 Street
Elmhurst, NY 11208
brightcuspdental@mailbox-example.com
www.brightcuspdental-example.com
I would like to present a very professional image for my company.
Smile!

```html
<!DOCTYPE html>
<html lang="en">
<head>
<meta charset="utf-8">
<title>Ron Talivero DDS – Stationery Package</title>
<link href="https://fonts.googleapis.com/css2?family=Lato:wght@400;700&display=swap" rel="stylesheet">
<style>
  :root{
    --bg-top:#5a5a5a;
    --bg-bottom:#2e2e2e;
    --paper:#ffffff;
    --ink:#4a4a4a;
    --green:#2f9a2c;
    --lime:#9cc524;
    --gold:#c9a51c;
    --black-card:#141414;
  }
  *{margin:0;padding:0;box-sizing:border-box}
  html,body{width:1200px;height:414px;overflow:hidden}
  body{
    position:relative;
    background:linear-gradient(180deg,var(--bg-top),var(--bg-bottom));
    font-family:"Lato",sans-serif;color:var(--ink);
  }
  .item{position:absolute;overflow:hidden;box-shadow:0 2px 6px rgba(0,0,0,.45)}
  .item svg.swoosh{position:absolute;left:0;bottom:0;width:100%}
  .brand{display:flex;align-items:center;gap:4px;color:var(--green);font-weight:700;white-space:nowrap}
  .brand .dot{border-radius:50%;background:currentColor;flex:none}
  .tagline{font-size:5px;color:var(--ink);white-space:nowrap}

  .logo-panel{position:absolute;left:20px;top:24px;width:150px;height:120px;box-shadow:none;
    display:flex;flex-direction:column;justify-content:center;padding-left:6px;gap:6px}
  .logo-panel .brand{font-size:15px;color:var(--lime)}
  .logo-panel .brand .dot{width:12px;height:12px}
  .logo-panel .tagline{color:#cfcfcf;font-size:7px}

  .card{width:96px;height:96px;padding:8px;font-size:4.6px;line-height:1.5}
  .card.wide{width:144px;height:92px}
  .card.white{background:var(--paper)}
  .card.dark{background:var(--black-card);color:#d8d8d8}
  .card.lime{background:linear-gradient(160deg,#d9e04a,var(--lime) 60%,#7aa51b)}
  .card.green{background:linear-gradient(160deg,#4fb43a,var(--green))}
  .card .name{font-size:6px;font-weight:700;color:var(--green);margin-bottom:3px}
  .card.dark .name{color:var(--lime)}
  .card .brand{font-size:8px}
  .card .brand .dot{width:6px;height:6px}
  .card.center{display:flex;flex-direction:column;align-items:center;justify-content:center;gap:3px}
  .card.dark .brand{color:var(--lime)}
  .card.green .brand,.card.lime .brand{color:#ffffff}
  .card .web{position:absolute;bottom:6px;right:8px;font-size:4.2px}

  .letterhead{left:480px;top:24px;width:216px;height:370px;background:var(--paper);padding:14px}
  .letterhead .brand{font-size:10px}
  .letterhead .brand .dot{width:8px;height:8px}
  .letterhead .contact{position:absolute;right:14px;top:14px;font-size:4.4px;line-height:1.55;text-align:left}

  .envelope{background:var(--paper);width:340px}
  .envelope-back{left:830px;top:56px;height:170px;background:#f4f4f4}
  .envelope-back svg{position:absolute;inset:0;width:100%;height:100%}
  .envelope-front{left:818px;top:234px;height:156px;padding:14px 16px}
  .envelope-front .brand{font-size:10px}
  .envelope-front .brand .dot{width:8px;height:8px}
  .envelope-front .address{font-size:4.6px;line-height:1.55;margin-top:6px}
</style>
</head>
<body>

  <div class="logo-panel">
    <div class="brand"><span class="dot"></span>brightcuspdental</div>
    <div class="tagline">General &amp; Cosmetic Dentistry</div>
  </div>

  <!-- business cards, row 1 -->
  <div class="item card white" style="left:187px;top:48px">
    <div class="name">RON TALIVERO DDS</div>
    <div>General &amp; Cosmetic Dentistry</div>
    <div>47-30 91 Street</div>
    <div>Elmhurst, NY 11208</div>
    <div>T: (718) 555-0142</div>
    <svg class="swoosh" viewBox="0 0 96 20" height="20" preserveAspectRatio="none"><path d="M0 14 Q48 2 96 10 L96 20 L0 20Z" fill="var(--green)"/><path d="M0 12 Q48 0 96 8 L96 10 Q48 3 0 15Z" fill="var(--gold)"/></svg>
  </div>
  <div class="item card white" style="left:300px;top:48px">
    <div class="name">Ron Talivero</div>
    <div>brightcuspdental@mailbox-example.com</div>
    <div>www.brightcuspdental-example.com</div>
    <div>T: (718) 555-0142</div>
    <svg class="swoosh" viewBox="0 0 96 20" height="20" preserveAspectRatio="none"><path d="M0 14 Q48 2 96 10 L96 20 L0 20Z" fill="var(--green)"/><path d="M0 12 Q48 0 96 8 L96 10 Q48 3 0 15Z" fill="var(--gold)"/></svg>
  </div>

  <!-- business cards, row 2 -->
  <div class="item card wide dark center" style="left:20px;top:163px">
    <div class="brand"><span class="dot"></span>brightcuspdental</div>
    <div class="tagline" style="color:#bbb">General &amp; Cosmetic Dentistry</div>
    <div class="web">www.brightcuspdental-example.com</div>
  </div>
  <div class="item card dark" style="left:187px;top:163px">
    <div class="name">RON TALIVERO DDS</div>
    <div>47-30 91 Street</div>
    <div>Elmhurst, NY 11208</div>
    <div>T: (718) 555-0142</div>
    <svg class="swoosh" viewBox="0 0 96 16" height="16" preserveAspectRatio="none"><path d="M0 12 Q48 0 96 8 L96 10 Q48 3 0 15Z" fill="var(--lime)"/></svg>
  </div>
  <div class="item card dark" style="left:300px;top:163px">
    <div class="name">Ron Talivero</div>
    <div>brightcuspdental@mailbox-example.com</div>
    <div>www.brightcuspdental-example.com</div>
    <svg class="swoosh" viewBox="0 0 96 16" height="16" preserveAspectRatio="none"><path d="M0 12 Q48 0 96 8 L96 10 Q48 3 0 15Z" fill="var(--gold)"/></svg>
  </div>

  <!-- business cards, row 3 -->
  <div class="item card wide white center" style="left:20px;top:280px">
    <div class="brand"><span class="dot"></span>brightcuspdental</div>
    <div class="tagline">General &amp; Cosmetic Dentistry</div>
    <div class="web">www.brightcuspdental-example.com</div>
  </div>
  <div class="item card lime center" style="left:187px;top:280px">
    <div class="brand"><span class="dot"></span>brightcuspdental</div>
  </div>
  <div class="item card green center" style="left:300px;top:280px">
    <div class="brand"><span class="dot"></span>brightcuspdental</div>
    <div class="web" style="color:#e6f2d8">www.brightcuspdental-example.com</div>
  </div>

  <!-- letterhead -->
  <div class="item letterhead">
    <div class="brand"><span class="dot"></span>brightcuspdental</div>
    <div class="tagline" style="margin-top:3px">General &amp; Cosmetic Dentistry</div>
    <div class="contact">
      <div>47-30 91 Street</div>
      <div>Elmhurst, NY 11208</div>
      <div>T: (718) 555-0142</div>
      <div>www.brightcuspdental-example.com</div>
    </div>
    <svg class="swoosh" viewBox="0 0 216 30" height="30" preserveAspectRatio="none"><path d="M0 22 Q108 4 216 14 L216 30 L0 30Z" fill="var(--green)"/><path d="M0 19 Q108 0 216 10 L216 13 Q108 4 0 23Z" fill="var(--gold)"/></svg>
  </div>

  <!-- envelopes -->
  <div class="item envelope envelope-back">
    <svg viewBox="0 0 340 170" preserveAspectRatio="none">
      <defs>
        <linearGradient id="flap" x1="0" y1="0" x2="1" y2="1">
          <stop offset="0" stop-color="#4fb43a"/><stop offset="1" stop-color="#1f7d22"/>
        </linearGradient>
      </defs>
      <path d="M0 0 L340 0 L340 40 Q170 110 0 40Z" fill="url(#flap)"/>
      <path d="M0 40 Q170 110 340 40 L340 58 Q170 122 0 58Z" fill="var(--gold)"/>
      <path d="M0 58 Q170 122 340 58" fill="none" stroke="#e6c94a" stroke-width="1.5"/>
    </svg>
  </div>
  <div class="item envelope envelope-front">
    <div class="brand"><span class="dot"></span>brightcuspdental</div>
    <div class="address">
      <div>47-30 91 Street</div>
      <div>Elmhurst, NY 11208</div>
    </div>
    <svg class="swoosh" viewBox="0 0 340 26" height="26" preserveAspectRatio="none"><path d="M0 20 Q170 2 340 14 L340 26 L0 26Z" fill="var(--green)"/><path d="M0 16 Q170 -2 340 10 L340 13 Q170 2 0 20Z" fill="var(--gold)"/></svg>
  </div>

</body>
</html>
```